Business Card Design

WE are looking for a premium quality Business Cards for a Law Firm . Copies of our current business card is attached.
Updates

Went on vacation/holiday

Contact Information for Business Card

xyz

```html
<!DOCTYPE html>
<html lang="en">
<head>
<meta charset="utf-8">
<title>Ashbury Lawyers – Business Cards</title>
<link href="https://fonts.googleapis.com/css2?family=Open+Sans:wght@400;600;700&display=swap" rel="stylesheet">
<style>
  :root {
    --backdrop: #d9d9d6;
    --card: #ffffff;
    --green: #0f2a1f;
    --gold: #c9a45c;
    --text: #1b2a23;
  }
  * { box-sizing: border-box; margin: 0; padding: 0; }
  html, body { width: 1200px; height: 801px; overflow: hidden; }
  body {
    background: var(--backdrop);
    font-family: "Open Sans", Arial, sans-serif;
    color: var(--text);
    position: relative;
  }
  .card {
    position: absolute;
    top: 245px;
    width: 540px;
    height: 310px;
    background: var(--card);
    border: 3px solid var(--gold);
    border-radius: 22px;
    box-shadow: 0 10px 24px rgba(0,0,0,.18);
  }
  .card--contact { left: 45px; }
  .card--brand { left: 615px; display: flex; align-items: center; justify-content: center; }

  .lockup { display: flex; flex-direction: column; align-items: center; }
  .lockup__ring {
    width: 78px; height: 78px;
    border: 5px solid var(--gold);
    border-radius: 50%;
    margin-bottom: 14px;
  }
  .lockup__name {
    font-weight: 700;
    color: var(--green);
    text-align: center;
    line-height: 1.1;
    font-size: 30px;
    letter-spacing: 1px;
  }
  .lockup__name span { display: block; font-size: 19px; letter-spacing: 9px; margin-top: 4px; padding-left: 9px; }
  .card--brand .lockup__ring { width: 110px; height: 110px; border-width: 6px; margin-bottom: 18px; }
  .card--brand .lockup__name { font-size: 42px; }
  .card--brand .lockup__name span { font-size: 25px; letter-spacing: 13px; padding-left: 13px; }

  .card--contact .lockup { position: absolute; left: 22px; top: 78px; width: 230px; }

  .divider {
    position: absolute;
    left: 262px; top: 36px;
    width: 1.5px; height: 238px;
    background: var(--green);
  }
  .details { position: absolute; left: 285px; top: 34px; right: 14px; }
  .details__name { font-size: 22px; font-weight: 700; color: var(--green); letter-spacing: .3px; }
  .details__role { font-size: 11.5px; line-height: 1.35; margin-top: 2px; }
  .contacts { list-style: none; margin-top: 14px; }
  .contacts li { display: flex; align-items: center; font-size: 12px; line-height: 1.6; }
  .contacts svg { width: 11px; height: 11px; margin-right: 8px; fill: var(--green); flex-shrink: 0; }
  .address { font-style: normal; font-size: 12px; line-height: 1.55; margin-top: 14px; }
</style>
</head>
<body>

<section class="card card--contact">
  <div class="lockup">
    <div class="lockup__ring"></div>
    <p class="lockup__name">ASHBURY<span>LAWYERS</span></p>
  </div>
  <div class="divider"></div>
  <div class="details">
    <h1 class="details__name">MARCUS HALE</h1>
    <p class="details__role">DIRECTOR &amp; PRINCIPAL SOLICITOR<br>MBA, Juris Doctor</p>
    <ul class="contacts">
      <li><svg viewBox="0 0 24 24"><path d="M6.6 10.8a15 15 0 006.6 6.6l2.2-2.2a1 1 0 011-.25 11.4 11.4 0 003.6.57 1 1 0 011 1V20a1 1 0 01-1 1A17 17 0 013 4a1 1 0 011-1h3.5a1 1 0 011 1c0 1.25.2 2.45.57 3.6a1 1 0 01-.25 1z"/></svg>+61 73000 0142</li>
      <li><svg viewBox="0 0 24 24"><path d="M7 1h10a2 2 0 012 2v18a2 2 0 01-2 2H7a2 2 0 01-2-2V3a2 2 0 012-2zm0 3v14h10V4zm5 15.5a1 1 0 100 2 1 1 0 000-2z"/></svg>+61 0400 000 318</li>
      <li><svg viewBox="0 0 24 24"><path d="M2 5h20v14H2zm2 2v.5l8 5 8-5V7z"/></svg>marcus@ashburylawyers.com.au</li>
      <li><svg viewBox="0 0 24 24"><path d="M12 2a10 10 0 100 20 10 10 0 000-20zm6.9 6h-3a15 15 0 00-1.3-3.9A8 8 0 0118.9 8zM12 4c.8 1.2 1.5 2.5 1.9 4h-3.8c.4-1.5 1.1-2.8 1.9-4zM4.3 14a8 8 0 010-4h3.4a16 16 0 000 4zm.8 2h3a15 15 0 001.3 3.9A8 8 0 015.1 16zm3-8h-3a8 8 0 014.3-3.9A15 15 0 008.1 8zM12 20c-.8-1.2-1.5-2.5-1.9-4h3.8c-.4 1.5-1.1 2.8-1.9 4zm2.3-6H9.7a14 14 0 010-4h4.6a14 14 0 010 4zm.3 5.9a15 15 0 001.3-3.9h3a8 8 0 01-4.3 3.9zm1.7-5.9a16 16 0 000-4h3.4a8 8 0 010 4z"/></svg>www.ashburylawyers.com.au</li>
    </ul>
    <address class="address">Level 3, Ashbury House,<br>48 Harlow Terrace,<br>Kelvin Grove, QLD 4059</address>
  </div>
</section>

<section class="card card--brand">
  <div class="lockup">
    <div class="lockup__ring"></div>
    <p class="lockup__name">ASHBURY<span>LAWYERS</span></p>
  </div>
</section>

</body>
</html>
```